Verdel Harvest Co - Business Card Design Project

We need business cards for our business. We grow roots and fruits in Central and South America, we import and distribute in FL, USA. We do fresh and frozen products.

Target Market(s)

Small and big supermarkets, wholesalers, traders, distributors, etc

Industry/Entity Type

Business

```html
<!DOCTYPE html>
<html lang="en">
<head>
<meta charset="UTF-8">
<title>Verdel Harvest Co – Business Card</title>
<link rel="stylesheet" href="https://fonts.googleapis.com/css2?family=Open+Sans:wght@400;600&display=swap">
<style>
  :root {
    --backdrop: #e9e9e6;
    --card: #fbfbf9;
    --leaf-green: #5e7d2f;
    --text-green: #667a3a;
    --accent-orange: #eea92f;
    --rule: #8a8a8a;
  }
  html, body {
    margin: 0;
    width: 1200px;
    height: 818px;
    overflow: hidden;
    background: var(--backdrop);
  }
  .stage {
    width: 1200px;
    height: 818px;
    display: flex;
    align-items: center;
    justify-content: center;
  }
  .business-card {
    position: relative;
    width: 420px;
    height: 720px;
    background: var(--card);
    box-shadow: 0 6px 22px rgba(0,0,0,0.14);
    overflow: hidden;
    font-family: "Open Sans", sans-serif;
    text-align: center;
  }
  .brand {
    margin-top: 78px;
  }
  .brand-name {
    font-size: 34px;
    font-weight: 600;
    color: var(--leaf-green);
    letter-spacing: 0.5px;
    margin: 0;
  }
  .brand-rule {
    width: 260px;
    height: 1px;
    background: var(--rule);
    margin: 12px auto 0;
  }
  .tagline {
    margin: 16px 0 0;
    font-size: 19px;
    color: var(--text-green);
  }
  .person {
    margin-top: 58px;
  }
  .person-name {
    margin: 0;
    font-size: 27px;
    color: var(--leaf-green);
  }
  .person-title {
    margin: 2px 0 0;
    font-size: 15px;
    color: var(--accent-orange);
  }
  .about {
    margin: 34px 0 0;
    font-size: 18px;
    line-height: 1.3;
    color: var(--text-green);
  }
  .distribution {
    margin: 22px 0 0;
    font-size: 18px;
    color: var(--text-green);
  }
  .corner-decoration {
    position: absolute;
    left: 0;
    bottom: 0;
    width: 300px;
    height: 230px;
  }
</style>
</head>
<body>
  <main class="stage">
    <article class="business-card">
      <header class="brand">
        <p class="brand-name">Verdel Harvest Co</p>
        <div class="brand-rule"></div>
        <p class="tagline">We do fresh and frozen products</p>
      </header>

      <section class="person">
        <p class="person-name">Employee Name</p>
        <p class="person-title">Managing Director</p>
      </section>

      <p class="about">We grow roots and fruits<br>in Central and South America</p>
      <p class="distribution">we import and distribute in FL, USA</p>

      <svg class="corner-decoration" viewBox="0 0 300 230" role="img" aria-label="Green foliage decoration in the lower corner">
        <defs>
          <radialGradient id="foliageTone" cx="0" cy="1" r="1">
            <stop offset="0" stop-color="#5e7d2f" stop-opacity="0.9"/>
            <stop offset="0.6" stop-color="#7a9648" stop-opacity="0.45"/>
            <stop offset="1" stop-color="#7a9648" stop-opacity="0"/>
          </radialGradient>
        </defs>
        <rect width="300" height="230" fill="url(#foliageTone)"/>
      </svg>
    </article>
  </main>
</body>
</html>
```